RK Website Home Page Design

The task is to develop a winning design for a replacement website for our client RK Plumbing, Heating, AC & Remodeling. ct

```html
<!DOCTYPE html>
<html lang="en">
<head>
<meta charset="utf-8">
<title>RK Plumbing, Heating, AC &amp; Remodeling</title>
<link href="https://fonts.googleapis.com/css2?family=Montserrat:wght@600;700;800;900&family=Poppins:wght@400;500;600;700&display=swap" rel="stylesheet">
<style>
:root{
  --navy:#0b2a78;
  --navy-deep:#071d57;
  --blue:#1746b8;
  --yellow:#f7d31b;
  --sky:#e8f0fb;
  --ink:#1d2433;
  --muted:#5b6478;
  --white:#ffffff;
}
*{box-sizing:border-box;margin:0;padding:0}
html,body{width:1200px;height:5228px;overflow:hidden;background:var(--white)}
body{position:relative;font-family:"Poppins",sans-serif;color:var(--ink)}
.abs{position:absolute}
h1,h2,h3,.heading{font-family:"Montserrat",sans-serif}
.btn{display:inline-block;font-family:"Montserrat",sans-serif;font-weight:700;font-size:14px;border-radius:22px;padding:10px 22px;text-decoration:none;color:var(--navy)}
.btn-yellow{background:var(--yellow)}
.btn-outline{background:var(--white);border:2px solid var(--navy)}
.hl{color:var(--yellow)}

/* header */
.site-header{top:0;left:0;width:1200px;height:150px;background:var(--white)}
.brand{left:40px;top:38px;display:flex;align-items:center;gap:12px}
.brand-dot{width:50px;height:50px;border-radius:50%;background:var(--yellow);flex:none}
.brand-name{font-family:"Montserrat",sans-serif;font-weight:800;font-size:18px;line-height:1.2;color:var(--navy);white-space:nowrap}
.serving{left:380px;top:38px;font-family:"Montserrat",sans-serif;font-weight:700;font-size:21px;color:var(--navy);white-space:nowrap}
.phones{left:380px;top:78px;display:flex;gap:36px}
.phone{display:flex;align-items:center;gap:10px;font-family:"Montserrat",sans-serif;font-weight:700;font-size:19px;color:var(--navy)}
.phone-icon{width:30px;height:30px;border-radius:50%;background:var(--yellow);display:flex;align-items:center;justify-content:center}
.header-actions{right:40px;top:24px;display:flex;flex-direction:column;gap:14px;align-items:stretch;width:190px;text-align:center}

.main-nav{top:150px;left:0;width:1200px;height:50px;background:var(--navy);display:flex;justify-content:center;align-items:center;gap:34px}
.main-nav a{color:var(--white);text-decoration:none;font-size:15px;font-weight:500}

/* hero */
.hero{top:200px;left:0;width:1200px;height:580px;overflow:hidden}
.hero-photo{position:absolute;inset:0;background:linear-gradient(100deg,#f4f6f9 0%,#eef0f3 35%,#c9d4e2 60%,#d9c3a8 80%,#e9e4dc 100%)}
.hero-copy{left:80px;top:130px}
.hero-copy h1{font-weight:900;font-size:42px;line-height:1.15;color:var(--navy);letter-spacing:.5px}
.hero-copy .btn{margin-top:30px}
.hero-wave{left:0;bottom:0;width:1200px;height:150px}

/* services */
.section-title{width:1200px;text-align:center;font-weight:900;font-size:32px;color:var(--navy)}
.service-grid{left:66px;width:1068px;display:grid;grid-template-columns:repeat(4,240px);column-gap:36px}
.service-card{position:relative;height:390px;background:var(--navy);clip-path:polygon(50% 0,100% 20%,100% 100%,0 100%,0 20%);color:var(--white);text-align:center;padding:96px 22px 0}
.service-card::after{content:"";position:absolute;inset:8px;clip-path:polygon(50% 0,100% 20%,100% 100%,0 100%,0 20%);box-shadow:inset 0 0 0 2px rgba(255,255,255,.35);pointer-events:none}
.service-card.is-active{background:var(--yellow);color:var(--navy)}
.service-icon{width:96px;height:96px;border-radius:50%;background:var(--white);margin:0 auto 22px;display:flex;align-items:center;justify-content:center}
.service-card h3{font-size:17px;font-weight:800;margin-bottom:10px}
.service-card p{font-size:12px;line-height:1.55;opacity:.9}
.read-more{display:inline-block;margin-top:14px;font-family:"Montserrat",sans-serif;font-weight:700;font-size:13px;color:var(--white);background:var(--navy);padding:6px 16px;border-radius:16px}

/* request */
.request{top:1770px;left:0;width:1200px;height:700px;background:var(--sky)}
.request-wave{top:0;left:0;width:1200px;height:110px}
.request-photo{left:40px;top:80px;width:520px;height:580px;border-radius:24px;background:linear-gradient(160deg,#f2f4f7 0%,#dfe5ee 45%,#c7cfdb 75%,#eef1f5 100%)}
.request-title{left:640px;top:90px;font-weight:900;font-size:30px;color:var(--navy)}
.request-form{left:640px;top:150px;width:490px;display:grid;grid-template-columns:1fr 1fr;gap:12px}
.field{height:40px;background:var(--white);border:1px solid #c5d0e3;font-size:14px;color:var(--muted);padding:9px 14px}
.field.full{grid-column:1/3;height:150px}
.request-form .btn{grid-column:1/2;width:110px;text-align:center;margin-top:6px}

/* reminder */
.reminder-copy{left:100px;top:2530px;width:520px}
.reminder-copy h2{font-weight:900;font-size:28px;color:var(--navy);margin-bottom:14px}
.reminder-copy p{font-size:15px;line-height:1.75;color:var(--ink)}
.reminder-photo{left:690px;top:2510px;width:270px;height:270px;border-radius:50%;border:10px solid var(--navy);box-shadow:0 0 0 6px var(--yellow);background:linear-gradient(150deg,#eaf0f7,#aab8cc 60%,#6c7c96)}

/* savings */
.savings{top:2890px;left:0;width:1200px;height:540px;background:linear-gradient(180deg,var(--blue),var(--navy))}
.savings h2{position:absolute;top:70px;width:1200px;text-align:center;font-weight:900;font-size:28px;line-height:1.25;color:var(--white)}
.coupons{position:absolute;top:170px;left:60px;display:flex;gap:30px}
.coupon{position:relative;width:340px;height:150px;border:2px dashed rgba(255,255,255,.6);border-radius:10px;padding:48px 104px 0 22px;color:var(--white)}
.coupon h3{font-size:17px;font-weight:800;white-space:nowrap}
.coupon p{font-size:13px;line-height:1.45;margin-top:6px}
.coupon-tag{position:absolute;top:-6px;right:16px;width:72px;height:92px;background:var(--yellow);clip-path:polygon(0 0,100% 0,100% 100%,50% 82%,0 100%);color:var(--navy);text-align:center;padding-top:12px;font-family:"Montserrat",sans-serif}
.coupon-tag small{display:block;font-size:12px;font-weight:700}
.coupon-tag strong{font-size:24px;font-weight:900}
.savings .btn{position:absolute;top:420px;left:524px}

/* difference */
.difference-photo{left:600px;top:3450px;width:600px;height:520px;background:linear-gradient(120deg,#f3f5f8 0%,#dfe4ea 40%,#c9b8a3 70%,#efe9e1 100%)}
.difference-copy{left:80px;top:3560px;width:500px}
.difference-copy h2{font-weight:900;font-size:26px;color:var(--navy);margin-bottom:16px;white-space:nowrap}
.difference-copy p{font-size:14px;line-height:1.75}
.difference-copy .btn{margin-top:26px}

/* blog */
.blog-grid{left:95px;top:4110px;display:flex;gap:25px}
.blog-card{width:320px;height:460px;background:var(--white);box-shadow:0 6px 24px rgba(11,42,120,.15);overflow:hidden}
.blog-image{height:200px}
.blog-body{padding:20px 22px}
.blog-date{font-size:12px;font-weight:600;color:var(--blue)}
.blog-card h3{font-size:17px;font-weight:800;color:var(--navy);margin:8px 0 10px;line-height:1.3}
.blog-card p{font-size:12px;line-height:1.6;color:var(--muted)}
.blog-more{left:540px;top:4620px}

/* footer */
.site-footer{top:4700px;left:0;width:1200px;height:528px;background:var(--navy);color:var(--white)}
.footer-wave{top:0;left:0;width:1200px;height:80px}
.footer-brand{left:100px;top:110px;width:340px}
.footer-brand .brand-name{color:var(--white);font-size:18px}
.footer-brand p{margin-top:22px;font-size:12px;line-height:1.7;opacity:.85}
.footer-col{top:120px}
.footer-col h3{font-size:24px;font-weight:800;margin-bottom:18px}
.link-columns{display:grid;grid-template-columns:150px 150px;row-gap:8px;font-size:13px}
.contact p{font-size:13px;line-height:1.9}
.payments{right:100px;top:405px;display:flex;gap:8px}
.payments span{width:44px;height:28px;border-radius:4px;background:var(--white)}
.footer-bar{left:0;bottom:0;width:1200px;height:56px;background:var(--navy-deep);display:flex;align-items:center;padding-left:100px;font-size:13px}
</style>
</head>
<body>

<header class="site-header abs">
  <div class="brand abs">
    <span class="brand-dot"></span>
    <span class="brand-name">RK Plumbing<br>Heating, AC &amp; Remodeling</span>
  </div>
  <div class="serving abs">Serving Millbrook, MA &amp; Neighboring Communities</div>
  <div class="phones abs">
    <span class="phone"><span class="phone-icon"><svg width="16" height="16" viewBox="0 0 24 24"><path fill="#0b2a78" d="M6.6 10.8a15.1 15.1 0 0 0 6.6 6.6l2.2-2.2c.3-.3.7-.4 1-.2 1.1.4 2.3.6 3.6.6.6 0 1 .4 1 1V20c0 .6-.4 1-1 1A17 17 0 0 1 3 4c0-.6.4-1 1-1h3.5c.6 0 1 .4 1 1 0 1.3.2 2.5.6 3.6.1.3 0 .7-.2 1z"/></svg></span>508.555.0142</span>
    <span class="phone"><span class="phone-icon"><svg width="16" height="16" viewBox="0 0 24 24"><path fill="#0b2a78" d="M6.6 10.8a15.1 15.1 0 0 0 6.6 6.6l2.2-2.2c.3-.3.7-.4 1-.2 1.1.4 2.3.6 3.6.6.6 0 1 .4 1 1V20c0 .6-.4 1-1 1A17 17 0 0 1 3 4c0-.6.4-1 1-1h3.5c.6 0 1 .4 1 1 0 1.3.2 2.5.6 3.6.1.3 0 .7-.2 1z"/></svg></span>800.555.0199</span>
  </div>
  <div class="header-actions abs">
    <a class="btn btn-yellow">Request Service</a>
    <a class="btn btn-outline">Request a Quote</a>
  </div>
</header>

<nav class="main-nav abs">
  <a>About</a><a>Plumbing</a><a>Water Heaters</a><a>Heating</a><a>Air Conditioning</a><a>Indoor Air Quality</a><a>Commercial</a><a>Remodeling</a><a>Contact</a>
</nav>

<section class="hero abs">
  <div class="hero-photo" role="img" aria-label="Family relaxing on a sofa with their dog beneath a wall-mounted air conditioner"></div>
  <div class="hero-copy abs">
    <h1>ENJOY THE BEST OF<br>HOME LIVING.<br>INDOORS &amp; OUT.</h1>
    <a class="btn btn-yellow">Contact Us To Get Started</a>
  </div>
  <svg class="hero-wave abs" viewBox="0 0 1200 150" preserveAspectRatio="none">
    <path d="M0 70 C300 150 700 150 1200 40 L1200 150 L0 150Z" fill="#f7d31b"/>
    <path d="M0 95 C320 165 720 160 1200 70 L1200 150 L0 150Z" fill="#0b2a78"/>
    <path d="M0 115 C340 175 760 170 1200 100 L1200 150 L0 150Z" fill="#ffffff"/>
  </svg>
</section>

<h2 class="section-title abs" style="top:815px">MORE OF WHAT <span class="hl">YOU NEED</span></h2>

<div class="service-grid abs" style="top:880px">
  <article class="service-card"><div class="service-icon"><svg width="56" height="56" viewBox="0 0 56 56"><rect x="8" y="22" width="30" height="10" fill="#1746b8"/><rect x="30" y="22" width="10" height="26" fill="#1746b8"/><circle cx="16" cy="18" r="6" fill="#f7d31b"/></svg></div><h3>Plumbing</h3><p>Lorem ipsum dolor sit amet, consectetur adipiscing elit, sed do eiusmod tempor incididunt ut.</p></article>
  <article class="service-card"><div class="service-icon"><svg width="56" height="56" viewBox="0 0 56 56"><rect x="16" y="6" width="24" height="44" rx="6" fill="#1746b8"/><circle cx="28" cy="36" r="6" fill="#f7d31b"/></svg></div><h3>Water Heaters</h3><p>Lorem ipsum dolor sit amet, consectetur adipiscing elit, sed do eiusmod tempor incididunt ut.</p></article>
  <article class="service-card"><div class="service-icon"><svg width="56" height="56" viewBox="0 0 56 56"><g fill="#c0392b"><rect x="10" y="10" width="6" height="36" rx="3"/><rect x="20" y="10" width="6" height="36" rx="3"/><rect x="30" y="10" width="6" height="36" rx="3"/><rect x="40" y="10" width="6" height="36" rx="3"/></g></svg></div><h3>Heating</h3><p>Lorem ipsum dolor sit amet, consectetur adipiscing elit, sed do eiusmod tempor incididunt ut.</p></article>
  <article class="service-card"><div class="service-icon"><svg width="56" height="56" viewBox="0 0 56 56"><rect x="6" y="16" width="44" height="18" rx="4" fill="#1746b8"/><path d="M16 40v8M28 40v8M40 40v8" stroke="#f7d31b" stroke-width="3"/></svg></div><h3>Air Conditioning</h3><p>Lorem ipsum dolor sit amet, consectetur adipiscing elit, sed do eiusmod tempor incididunt ut.</p></article>
</div>

<div class="service-grid abs" style="top:1330px">
  <article class="service-card"><div class="service-icon"><svg width="56" height="56" viewBox="0 0 56 56"><path d="M8 20h30a6 6 0 1 0-6-6M8 30h38a6 6 0 1 1-6 6M8 40h20" stroke="#1746b8" stroke-width="4" fill="none"/></svg></div><h3>Indoor Air Quality</h3><p>Lorem ipsum dolor sit amet, consectetur adipiscing elit, sed do eiusmod tempor incididunt ut.</p></article>
  <article class="service-card is-active"><div class="service-icon"><svg width="56" height="56" viewBox="0 0 56 56"><path d="M28 6C20 18 14 26 14 34a14 14 0 0 0 28 0c0-8-6-16-14-28z" fill="#1746b8"/></svg></div><h3>Water Filtration</h3><p>Lorem ipsum dolor sit amet, consectetur adipiscing elit, sed do eiusmod tempor incididunt ut.</p><span class="read-more">Read More</span></article>
  <article class="service-card"><div class="service-icon"><svg width="56" height="56" viewBox="0 0 56 56"><path d="M6 28L28 8l22 20" stroke="#1746b8" stroke-width="4" fill="none"/><rect x="14" y="28" width="28" height="20" fill="#1746b8"/><rect x="24" y="36" width="8" height="12" fill="#f7d31b"/></svg></div><h3>Remodeling</h3><p>Lorem ipsum dolor sit amet, consectetur adipiscing elit, sed do eiusmod tempor incididunt ut.</p></article>
  <article class="service-card"><div class="service-icon"><svg width="56" height="56" viewBox="0 0 56 56"><path d="M28 6c4 10 14 14 14 28a14 14 0 0 1-28 0c0-8 6-12 8-18 2 6 6 6 6 0z" fill="#f39c12"/></svg></div><h3>Gas Fireplaces</h3><p>Lorem ipsum dolor sit amet, consectetur adipiscing elit, sed do eiusmod tempor incididunt ut.</p></article>
</div>

<section class="request abs">
  <svg class="request-wave abs" viewBox="0 0 1200 110" preserveAspectRatio="none"><path d="M0 0H1200V20C800 110 400 110 0 30Z" fill="#ffffff"/></svg>
  <div class="request-photo abs" role="img" aria-label="Smiling technician holding a remote beside an air conditioning unit and a branded service van"></div>
  <h2 class="request-title abs">REQUEST <span class="hl">SERVICE</span></h2>
  <form class="request-form abs">
    <div class="field">Name*</div><div class="field">Address</div>
    <div class="field">City</div><div class="field">Zip</div>
    <div class="field">Phone</div><div class="field">Email*</div>
    <div class="field full">Message</div>
    <a class="btn btn-yellow">Submit</a>
  </form>
</section>

<div class="reminder-copy abs">
  <h2>BACK TO SCHOOL <span class="hl">REMINDER</span></h2>
  <p>Most families see an uptick in morning “rush hour” activity once the school year begins and so does your water heater. Can yours keep up with the increased demand? Contact us today for a water heater check-up and free quote on a replacement system.</p>
</div>
<div class="reminder-photo abs" role="img" aria-label="Two plumbers standing together with their tools"></div>

<section class="savings abs">
  <h2>ENJOY THE SAVINGS...<br><span class="hl">PLUS THE ADDED COMFORT!</span></h2>
  <div class="coupons">
    <div class="coupon"><div class="coupon-tag"><small>Save</small><strong>$120</strong></div><h3>New Water Heater</h3><p>...on a new water heater, tank-style or tankless.</p></div>
    <div class="coupon"><div class="coupon-tag"><small>Save</small><strong>$350</strong></div><h3>HVAC System</h3><p>...on a new heating or cooling system.</p></div>
    <div class="coupon"><div class="coupon-tag"><small>Save</small><strong>$35</strong></div><h3>First-time Customer</h3><p>...on any service we provide.</p></div>
  </div>
  <a class="btn btn-yellow">Click For Details</a>
</section>

<div class="difference-photo abs" role="img" aria-label="Happy couple relaxing together at home"></div>
<div class="difference-copy abs">
  <h2>THE RK DIFFERENCE <span class="hl">MAKERS</span></h2>
  <p>RK is a favorite choice among homeowners who appreciate our extensive range of home comfort and related services. Others like us best for our 100% satisfaction guarantee, while still others enjoy the many benefits that membership in our Preferred Service Club provides. Add it all up, and there’s a lot to like about RK Plumbing, Heating, AC &amp; Remodeling.</p>
  <a class="btn btn-yellow">Learn More</a>
</div>

<h2 class="section-title abs" style="top:4040px">LATEST <span class="hl">BLOG</span></h2>
<div class="blog-grid abs">
  <article class="blog-card"><div class="blog-image" role="img" aria-label="Technician servicing an air conditioning unit" style="background:linear-gradient(135deg,#dfe6ef,#9fb1c9)"></div><div class="blog-body"><div class="blog-date">MAY 31, 2022</div><h3>The Benefits of an AC Tune-Up</h3><p>Here are tips to prepare your home for spring and summer so your AC runs cool, quiet and efficient season.</p></div></article>
  <article class="blog-card"><div class="blog-image" role="img" aria-label="Ductless air conditioner on a living room wall" style="background:linear-gradient(135deg,#f1f3f6,#c3ccd8)"></div><div class="blog-body"><div class="blog-date">MAY 31, 2022</div><h3>Beat the Summer Heat with Ductless Air</h3><p>Ductless mini splits bring quiet, efficient cooling to rooms without ductwork, making them a smart choice for many older homes.</p></div></article>
  <article class="blog-card"><div class="blog-image" role="img" aria-label="Water leaking under a kitchen sink" style="background:linear-gradient(135deg,#e6ecf3,#8fa3bd)"></div><div class="blog-body"><div class="blog-date">MAY 31, 2022</div><h3>What Not to Do as a Homeowner</h3><p>Even a small leak can turn into costly damage. Learn the first steps to take before your plumber arrives today.</p></div></article>
</div>
<a class="btn btn-yellow blog-more abs">View More</a>

<footer class="site-footer abs">
  <svg class="footer-wave abs" viewBox="0 0 1200 80" preserveAspectRatio="none"><path d="M0 0H1200V10C800 80 400 80 0 20Z" fill="#ffffff"/><path d="M0 20C400 80 800 80 1200 10" stroke="#f7d31b" stroke-width="4" fill="none"/></svg>
  <div class="footer-brand abs">
    <div class="brand" style="position:static"><span class="brand-dot"></span><span class="brand-name">RK Plumbing<br>Heating, AC &amp; Remodeling</span></div>
    <p>RK Plumbing, Heating &amp; AC was started in 1986 by a local family who built the business into a trusted home services name.</p>
  </div>
  <div class="footer-col abs" style="left:500px">
    <h3>Quick Link</h3>
    <div class="link-columns"><span>About</span><span>Indoor Air Quality</span><span>Plumbing</span><span>Commercial</span><span>Water Heaters</span><span>Work Samples</span><span>Heating</span><span>Remodeling</span><span>Air Conditioning</span><span>Contact</span></div>
  </div>
  <div class="footer-col contact abs" style="left:880px">
    <h3>Contact Us</h3>
    <p>125 Harbor Street, Millbrook, MA 01700<br>Local: 508.555.0142<br>Toll Free: 800.555.0199<br>info@rkplumbing.example</p>
  </div>
  <div class="payments abs" aria-label="Accepted payment methods"><span></span><span></span><span></span><span></span><span></span></div>
  <div class="footer-bar abs">© 2022 RK Heating &amp; Plumbing | All Rights Reserved</div>
</footer>

</body>
</html>
```